Business card for hi tech component manufacturer, specialising in after market firearms components a
Tovin Industries (Ti)
Use same font as used in my logo
Owen Petrie
General Manager
Postal: PO Box 58491, Brackley, Christchurch 8245, New Zealand
Physical: 14 Garnet Street, Fenwick, Christchurch 8024, New Zealand
sales@tovin-works.example.nz
tovin-works.example.nz
Details are to be confirmed in future. Please allow space for Addresses, Phone, Cell, Email and Web address.
Hi Quill42,
You are the winner of the stationary project for Tovin Industries.
We have had some commercial issues with the company name Tovin, and as this is a start up company, we have changed the name.
The new Company name is ZENTH Industries. I have the new logo file, how do I send this to you?
As such I have a new set of address and company name for you to change for the final design.
And the only contact details we want on all the stationary options that you supplied are as follows:
Web: www.zenth.example.nz
Email address: sales@zenth.example.nz
Phone: +6429184306
Contact: Owen Petrie General Manager
Please advise, if you require a different file type, I have .ai, .eps, .gif, .pdf, .png, .psd, .jpg, .tif
I look forward to hearing from you.
Best regards,
Owen

```html
<!DOCTYPE html>
<html lang="en">
<head>
<meta charset="utf-8">
<title>ZENTH Industries – Business Card</title>
<link rel="stylesheet" href="https://fonts.googleapis.com/css2?family=Michroma&family=Jura:wght@400;500&display=swap">
<style>
  :root {
    --backdrop: #e4e4e2;
    --card: #ffffff;
    --ink: #2b2b2b;
    --steel-blue: #3d5f78;
    --muted: #5a5a5a;
  }
  html, body {
    margin: 0;
    width: 1200px;
    height: 900px;
    overflow: hidden;
    background: var(--backdrop);
  }
  .card {
    position: absolute;
    left: 110px;
    top: 170px;
    width: 980px;
    height: 560px;
    background: var(--card);
    box-shadow: 0 2px 10px rgba(0,0,0,0.12);
    overflow: hidden;
  }
  .wordmark {
    position: absolute;
    left: 60px;
    top: 74px;
    margin: 0;
    font-family: "Michroma", sans-serif;
    font-weight: 400;
    font-size: 34px;
    letter-spacing: 3px;
    color: var(--ink);
    text-transform: uppercase;
  }
  .brand-block {
    position: absolute;
    right: 70px;
    top: 150px;
    width: 300px;
    height: 300px;
    background: var(--steel-blue);
  }
  .person {
    position: absolute;
    left: 60px;
    top: 196px;
    font-family: "Jura", sans-serif;
    font-variant: small-caps;
    letter-spacing: 1px;
  }
  .person-name {
    margin: 0;
    font-size: 26px;
    font-weight: 500;
    color: var(--steel-blue);
  }
  .person-role {
    margin: 2px 0 0;
    font-size: 22px;
    font-weight: 500;
    color: var(--ink);
  }
  .contacts {
    position: absolute;
    left: 60px;
    top: 432px;
    margin: 0;
    padding: 0;
    list-style: none;
    font-family: "Jura", sans-serif;
    font-variant: small-caps;
    font-size: 15px;
    font-weight: 500;
    letter-spacing: 0.8px;
    color: var(--muted);
    line-height: 19px;
  }
  .contact-line {
    display: flex;
    gap: 12px;
  }
  .contact-icon {
    flex: none;
    width: 14px;
    height: 14px;
    margin-top: 2px;
  }
</style>
</head>
<body>
  <article class="card">
    <h1 class="wordmark">ZENTH Industries</h1>
    <div class="brand-block" aria-hidden="true"></div>

    <div class="person">
      <p class="person-name">Owen Petrie</p>
      <p class="person-role">General Manager</p>
    </div>

    <ul class="contacts">
      <li class="contact-line">
        <svg class="contact-icon" viewBox="0 0 14 14" aria-hidden="true"><circle cx="7" cy="7" r="7" fill="var(--muted)"/><path d="M5 3.5l1.2 2-0.8 0.8a5 5 0 0 0 2.3 2.3l0.8-0.8 2 1.2-0.6 1.3C7.2 10.6 3.4 6.8 3.7 4.1z" fill="#fff"/></svg>
        <span>+64 29 184 306</span>
      </li>
      <li class="contact-line">
        <svg class="contact-icon" viewBox="0 0 14 14" aria-hidden="true"><circle cx="7" cy="7" r="7" fill="var(--muted)"/><rect x="3.5" y="4.5" width="7" height="5" fill="#fff"/><path d="M3.5 4.5L7 7.3l3.5-2.8" stroke="var(--muted)" stroke-width="0.8" fill="none"/></svg>
        <span>sales@zenth.example.nz</span>
      </li>
      <li class="contact-line">
        <svg class="contact-icon" viewBox="0 0 14 14" aria-hidden="true"><circle cx="7" cy="7" r="7" fill="var(--muted)"/><circle cx="7" cy="7" r="3.6" fill="none" stroke="#fff" stroke-width="0.9"/><path d="M3.4 7h7.2M7 3.4c-1.6 2-1.6 5.2 0 7.2M7 3.4c1.6 2 1.6 5.2 0 7.2" stroke="#fff" stroke-width="0.8" fill="none"/></svg>
        <span>www.zenth.example.nz</span>
      </li>
    </ul>
  </article>
</body>
</html>
```